"Quill Romper" Soil Conditioner for Lawn and Garden.

I need a product label with logo for a square 1 qt F Style plastic Bottle. The area would be 3.75" wide x 4.125" Tall front and back panel. Needs plenty of text area on the back panel.

Target Market(s)

Landscape and Garden

Industry/Entity Type

Home and Garden

Requirements
Must have
• Focus on the problems of heavy soils

```html
<!DOCTYPE html>
<html lang="en">
<head>
<meta charset="utf-8">
<title>Quill Romper Soil Conditioner Label</title>
<link rel="stylesheet" href="https://fonts.googleapis.com/css2?family=Bebas+Neue&family=Poppins:wght@400;600;700&display=swap">
<style>
  :root {
    --soil-dark: #0d1a0b;
    --leaf-green: #7ed321;
    --badge-green: #9be05a;
    --tag-green: #0f3a0b;
    --white: #ffffff;
    --soft-white: #f1f7e8;
  }
  * { margin: 0; padding: 0; box-sizing: border-box; }
  html, body { width: 1090px; height: 1200px; overflow: hidden; background: var(--soil-dark); }
  .label {
    position: relative;
    width: 1090px;
    height: 1200px;
    overflow: hidden;
    font-family: "Poppins", sans-serif;
    color: var(--white);
  }
  .soil-photo {
    position: absolute; inset: 0;
    background:
      radial-gradient(ellipse 60% 35% at 50% 52%, rgba(5,10,5,0.85), rgba(5,10,5,0) 70%),
      radial-gradient(ellipse 55% 30% at 80% 75%, #2b3527 0%, rgba(43,53,39,0) 70%),
      linear-gradient(180deg, #2f4a1e 0%, #3a4a30 22%, #2c3a2a 45%, #1c2a1a 65%, #1e3a14 88%, #24521a 100%);
  }
  .badge {
    position: absolute; left: 296px; top: 81px;
    display: flex; align-items: center; gap: 28px;
  }
  .badge-dot {
    width: 62px; height: 62px; border-radius: 50%;
    background: var(--badge-green);
    flex: none;
  }
  .badge-text {
    font-family: "Bebas Neue", sans-serif;
    font-size: 79px; line-height: 1; letter-spacing: 0.5px;
  }
  .badge-text .figure { color: var(--soft-white); }
  .badge-text .word { color: var(--badge-green); }
  .headline {
    position: absolute; left: 0; right: 0;
    text-align: center;
    font-family: "Bebas Neue", sans-serif;
    font-size: 272px; line-height: 1;
  }
  .headline-top { top: 290px; color: var(--white); }
  .headline-bottom { top: 497px; color: var(--leaf-green); }
  .subtitle {
    position: absolute; left: 0; right: 0; text-align: center;
    font-family: "Bebas Neue", sans-serif; line-height: 1; letter-spacing: -0.5px;
  }
  .subtitle-top { top: 750px; font-size: 68px; color: var(--white); }
  .subtitle-bottom { top: 808px; font-size: 66px; color: var(--leaf-green); }
  .tag {
    position: absolute;
    height: 34px;
    padding: 0 19px;
    background: var(--tag-green);
    color: var(--leaf-green);
    font-family: "Bebas Neue", sans-serif;
    font-size: 23px; line-height: 36px; letter-spacing: 0.5px;
  }
  .tag-usages { left: 91px; top: 928px; }
  .tag-instruction { left: 91px; top: 1038px; }
  .tag-caution { left: 731px; top: 928px; }
  .body-copy {
    position: absolute;
    font-size: 20px; line-height: 22px; color: var(--white);
    white-space: nowrap;
  }
  .usages-copy { left: 90px; top: 963px; }
  .instruction-copy { left: 96px; top: 1078px; }
  .divider {
    position: absolute; left: 650px; top: 952px;
    width: 1px; height: 150px; background: rgba(10,30,8,0.7);
  }
  .caution-copy {
    position: absolute; left: 735px; top: 967px;
    font-weight: 700; font-size: 22px; line-height: 22px;
    white-space: nowrap;
  }
  .volume {
    position: absolute; left: 731px; top: 1038px;
    width: 259px; height: 87px;
    background: var(--tag-green);
    color: var(--leaf-green);
    font-family: "Bebas Neue", sans-serif;
    font-size: 37px; line-height: 89px; text-align: center; letter-spacing: -1px;
  }
</style>
</head>
<body>
<main class="label">
  <div class="soil-photo" role="img" aria-label="Close-up photograph of dark, crumbly garden soil with a blurred green plant in the background"></div>

  <div class="badge">
    <span class="badge-dot" aria-hidden="true"></span>
    <div class="badge-text"><span class="figure">100%</span> <span class="word">Effective</span></div>
  </div>

  <h1 class="headline headline-top">Quill</h1>
  <div class="headline headline-bottom">Romper</div>

  <div class="subtitle subtitle-top">Soil Conditioner for</div>
  <div class="subtitle subtitle-bottom">Landscape and Garden:</div>

  <div class="tag tag-usages">Usages:</div>
  <p class="body-copy usages-copy">Promotes soil drainage and alleviates puddling<br>and dry spots by opening more pore space<br>for water and air on contact.</p>

  <div class="tag tag-instruction">Instruction:</div>
  <p class="body-copy instruction-copy">Lightly apply 1 oz./gal of water with a hose end<br>sprayer, and then water in.</p>

  <div class="divider"></div>

  <div class="tag tag-caution">Caution:</div>
  <p class="caution-copy">KEEP OUT OF REACH<br>OF CHILDREN!</p>

  <div class="volume">1 Quart (32 FL.OZ.)</div>
</main>
</body>
</html>
```